Homepage layout for online ad network

Attached is our Valtry Media logo and updated brief (I can't seem to delete the old logo and brief, but they're no longer relevant).

This project was originally posted with a different logo and corporate name, but we have decided to stay with our current logo and name and redesign the site.

Your design is for a homepage only - design, no coding (I'll get someone else to take your PSD and code it).

Your homepage will make use of a Flash slider - BUT YOU ARE NOT REQUIRED TO PROVIDE THE FLASH. Instead, simply provide the layout and at least two static examples out of the four different sections that will eventually be in the slider.

Much of this design is based on the design of a competitor (listed in the brief).

Please ask whatever questions you need to in order to clarify instructions.
Updates

Project updated to include new logo (and correspondingly new color scheme).

Brief changed slightly.

Thank you for submitting designs for this project in the past.

After some internal strategy work, we have decided to retain our initial corporate identity, Valtry Media.

If you have submitted a design for the original brief and are available, please re-work your best prior design to reflect the color scheme in the newly uploaded logo.

Target Market(s)

This site is aimed primarily at young professionals who buy digital media on behalf of large advertisers.

Industry/Entity Type

Media

Requirements
Must have
• modern white space
Should not have
• no Flash outside of slider

```html
<!DOCTYPE html>
<html lang="en">
<head>
<meta charset="utf-8">
<title>Valtry Media — Home</title>
<link rel="stylesheet" href="https://fonts.googleapis.com/css2?family=Arimo:wght@400;700&display=swap">
<style>
:root{
  --red:#c0272d;
  --red-dark:#b10000;
  --red-band:#a8383c;
  --ink:#222;
  --ink-soft:#444;
  --news-red:#a81c1c;
  --white:#fff;
  --grey-panel:#f1f1f1;
  --footer:#000;
  --dot:#d23a32;
}
*{margin:0;padding:0;box-sizing:border-box}
html,body{width:1200px;height:900px;overflow:hidden;background:var(--white);font-family:"Arimo",Arial,sans-serif;color:var(--ink)}
.page{position:relative;width:1200px;height:900px}
.abs{position:absolute}

/* header */
.brand{left:170px;top:40px;display:flex;align-items:center;gap:14px}
.brand-mark{display:block;width:40px;height:40px;background:var(--red)}
.brand-name{font-size:34px;line-height:40px;color:var(--ink);font-weight:400}
.tagline{left:172px;top:96px;font-size:13px;color:var(--ink-soft)}
.utility{left:816px;top:74px;font-size:12px;color:#000}
.flags{left:1020px;top:73px;display:flex;gap:10px}
.flags svg{display:block;border:1px solid #777}
.rule-dotted{left:0;width:1200px;height:0;border-top:2px dotted #ccc}

/* nav */
.nav-band{left:0;top:122px;width:1200px;height:48px;background:linear-gradient(var(--red-band) 0 50%,var(--red-dark) 50% 100%)}
.nav{left:729px;top:132px;display:flex;list-style:none}
.nav li{height:38px;line-height:34px;font-size:14px;color:var(--white);text-align:center}
.nav .beauty{width:71px;background:linear-gradient(#fff,#e4e4e4);color:#000}
.nav .cooking{width:88px}
.nav .parenting{width:108px}
.nav .video{width:89px}

/* hero */
.hero-side{top:170px;width:101px;height:310px;background:repeating-linear-gradient(45deg,#262626 0 2px,#1d1d1d 2px 4px)}
.hero-frame{left:101px;top:170px;width:998px;height:290px;background:var(--white)}
.hero-visual{left:107px;top:176px;width:985px;height:274px;background:linear-gradient(90deg,#3a0806 0%,#b8260f 25%,#e3542a 42%,#3b2a22 60%,#4d3f37 80%,#2a2421 100%)}
.hero-title{left:162px;top:242px;font-size:21px;color:var(--white)}
.hero-copy{left:160px;top:274px;font-size:16px;line-height:24px;color:var(--white);width:290px}
.hero-btn{left:302px;top:345px;width:122px;height:33px;border-radius:4px;background:linear-gradient(#f4f8fb,#a9c3d4);color:#111;font-size:16px;text-align:center;line-height:33px}
.hero-arrow{top:295px}
.slider-bar{left:101px;top:456px;width:998px;height:24px;background:linear-gradient(#9a9a9a,#fff 35%)}
.dots{left:602px;top:460px;display:flex;gap:7px}
.dots span{width:14px;height:14px;border-radius:50%;background:var(--dot)}
.dots .on{background:#000}

/* content */
.hatch{top:480px;height:350px;background:repeating-linear-gradient(135deg,#fff 0 2px,#d9d9d9 2px 3px)}
.content{left:100px;top:480px;width:1000px;height:350px;background:var(--white)}
.section-title{left:134px;top:496px;font-size:29px;font-weight:400;color:var(--ink)}
.section-title em{font-style:normal;color:var(--red)}
.section-rule{left:134px;top:535px;width:476px;border-top:2px dashed #ccc}
.section-sub{left:134px;top:546px;font-size:16px;color:var(--ink-soft)}
.card-panel{left:108px;top:580px;width:650px;height:218px;border-radius:6px;background:linear-gradient(#fff,var(--grey-panel))}
.card{width:172px;height:191px;border:1px solid #222;border-radius:6px;background:#fafafa;overflow:hidden;top:595px}
.card-image{position:absolute;left:8px;top:15px;width:151px;height:112px;border:1px solid #222;border-radius:5px}
.card-caption{position:absolute;left:0;bottom:0;width:100%;height:48px;background:linear-gradient(#4a4a4a,#111);color:var(--white);font-size:13px;line-height:20px;padding:4px 0 0 15px}

/* news */
.news{left:787px;top:498px;width:301px;height:290px;border:1px solid #333;border-radius:7px;background:linear-gradient(160deg,#fff 55%,#e9e9e9);overflow:hidden}
.news-icon{position:absolute;left:13px;top:8px;width:40px;height:32px;background:linear-gradient(#eee,#bbb);border:1px solid #999}
.news-title{position:absolute;left:70px;top:2px;font-size:40px;font-weight:400;color:#d33a2c}
.news-list{position:absolute;left:16px;top:47px;width:270px;list-style:none;font-size:12px;line-height:24px}
.news-list time{display:block;color:var(--news-red)}
.news-list p{text-align:justify;color:#000;letter-spacing:.3px}

/* footer */
.footer{left:0;top:831px;width:1200px;height:69px;background:var(--footer)}
.footer-links{width:1200px;top:855px;text-align:center;font-size:12px;color:var(--white)}
.footer-links span{margin:0 9px}
</style>
</head>
<body>
<div class="page">

  <header>
    <div class="abs brand"><span class="brand-mark"></span><span class="brand-name">Valtry Media</span></div>
    <div class="abs tagline">the right audience for every brand</div>
    <nav class="abs utility">Contact Us | Careers | Client Login</nav>
    <div class="abs flags">
      <svg width="24" height="16" viewBox="0 0 24 16" aria-label="English (US)">
        <rect width="24" height="16" fill="#fff"/>
        <g fill="#c33"><rect y="0" width="24" height="2"/><rect y="4" width="24" height="2"/><rect y="8" width="24" height="2"/><rect y="12" width="24" height="2"/></g>
        <rect width="10" height="8" fill="#34588c"/>
      </svg>
      <svg width="24" height="16" viewBox="0 0 24 16" aria-label="English (UK)">
        <rect width="24" height="16" fill="#2a4b8d"/>
        <path d="M0 0L24 16M24 0L0 16" stroke="#fff" stroke-width="3"/>
        <path d="M12 0V16M0 8H24" stroke="#fff" stroke-width="5"/>
        <path d="M12 0V16M0 8H24" stroke="#c33" stroke-width="3"/>
      </svg>
    </div>
    <div class="abs rule-dotted" style="top:115px"></div>
  </header>

  <div class="abs nav-band"></div>
  <ul class="abs nav">
    <li class="beauty">Beauty</li>
    <li class="cooking">Cooking</li>
    <li class="parenting">Parenting</li>
    <li class="video">Video</li>
  </ul>

  <section class="hero">
    <div class="abs hero-side" style="left:0"></div>
    <div class="abs hero-side" style="left:1099px"></div>
    <div class="abs hero-frame"></div>
    <div class="abs hero-visual" role="img" aria-label="Red fiery light streaks beside a chef stir-frying vegetables in a smoking wok"></div>
    <div class="abs hero-title">Cooking</div>
    <p class="abs hero-copy">Lorem Ipsum is simply dummy text of the printing and typesetting industry.</p>
    <div class="abs hero-btn">Learn More</div>
    <svg class="abs hero-arrow" style="left:41px" width="38" height="38" viewBox="0 0 38 38" aria-label="Previous slide">
      <circle cx="19" cy="19" r="17" fill="none" stroke="#fff" stroke-width="2"/>
      <path d="M23 9L11 19L23 29L20 19Z" fill="#fff"/>
    </svg>
    <svg class="abs hero-arrow" style="left:1121px" width="38" height="38" viewBox="0 0 38 38" aria-label="Next slide">
      <circle cx="19" cy="19" r="17" fill="none" stroke="#fff" stroke-width="2"/>
      <path d="M15 9L27 19L15 29L18 19Z" fill="#fff"/>
    </svg>
    <div class="abs slider-bar"></div>
    <div class="abs dots"><span></span><span class="on"></span><span></span><span></span></div>
  </section>

  <div class="abs hatch" style="left:0;width:100px"></div>
  <div class="abs hatch" style="left:1100px;width:100px"></div>
  <main class="abs content"></main>

  <h1 class="abs section-title"><em>Valtry</em> Media</h1>
  <div class="abs section-rule"></div>
  <p class="abs section-sub">Advanced Valtry Media insights for marketers</p>

  <div class="abs card-panel"></div>
  <article class="abs card" style="left:128px">
    <div class="card-image" role="img" aria-label="Two people leaping toward each other against a blue sky, forming a heart shape" style="background:linear-gradient(#6d9ad0,#b6cfe8 70%,#d9c9b0)"></div>
    <div class="card-caption">Kinetic delivers<br>a 71% ROI. Sweet!</div>
  </article>
  <article class="abs card" style="left:339px">
    <div class="card-image" role="img" aria-label="Blue 2010 report book standing upright" style="left:9px;background:linear-gradient(90deg,#fff 25%,#3d6aa8 40%,#6f93c4 60%,#fff 75%)"></div>
    <div class="card-caption" style="padding-left:18px">2010 Display<br>Advertising Study</div>
  </article>
  <article class="abs card" style="left:560px">
    <div class="card-image" role="img" aria-label="Goldfish jumping between two glass fishbowls" style="left:12px;background:linear-gradient(#fff 30%,#d7e6f2 60%,#f2a55a 75%,#fff)"></div>
    <div class="card-caption" style="height:41px;padding-top:0;padding-left:21px">Display Advertising<br>Engagement on the Rise</div>
  </article>

  <aside class="abs news">
    <div class="news-icon" role="img" aria-label="Newspaper icon"></div>
    <h2 class="news-title">News</h2>
    <ul class="news-list">
      <li><time>September 29, 2010</time><p>Kinetic Reach does a good job of homepage design</p></li>
      <li><time>September 24, 2010</time><p>Giving the brand the right audience</p></li>
      <li><time>September 16, 2010</time><p>Kinetic Launches in the UK</p></li>
      <li><time>September 8, 2010</time><p>Kinetic Taps Brightpath, Corvane, Veerly, and Clipvale.tv</p></li>
    </ul>
  </aside>

  <div class="abs rule-dotted" style="top:828px;left:108px;width:992px"></div>
  <footer class="abs footer"></footer>
  <nav class="abs footer-links">About us<span>|</span>Contact Us<span>|</span>Management Team<span>|</span>News<span>|</span>Careers</nav>

</div>
</body>
</html>
```